Human Resources consulting firm website

I recently started a consulting firm after 30 years in Human Resources (Executive Development) work with Meridian 25 companies. I am looking for a website design that will convey both the services I provide (all in the HR / executive development arena) as well as sense of trust in me and my abilities (many years of experience, breadth of knowledge).

In the attachment section, there is a document with links to a number of websites fr firms that do similar work to me - the doc shares what I like about them and what I do not. I've also include my bio to give you a sens of who I am /what I do. The head shot will be replaced soon as I'm having new photos take, but the verbiage is what's important.

I need your help with the look and feel as well as different ideas on how to share the info. I am looking for your creativity and experience. I have not done a website for anything in the past.

Looking forward to working together on a great project and product!!

Target Market(s)

Any company looking for senior leader caoching, assessments of those leaders or help with a CEO transition. My wheelhouse is Meridian top 100 companies, but am able to work with small firms as well. Also any Board of Directors and upstarts in California.

Industry/Entity Type

Consulting

Coding

Coded - Design and coding required

Number of Pages Required

5+ page

Font styles to use
Sans Serif
Other font styles liked:
• Do not have a specific one but am very open to options

Colors

Designer to choose colors to be used in the design.

Requirements
Must have
• My project must have be professional (see the type of companies I am targeting) with an air of simplicity.
• A professional yet approachable look and feel that delivers:
• (1) I want there to be a landing page (with limited info - a more of a "teaser")
• (2) a tab for about us (with a few sentences about the company, my photo and option to link to my bio)
• (3) a tab for the services offered (one page with tiles that have a little bit about the services and the option to link to more info)
• (4) a tab to contact me (form to fill out with some personal info and the request that will get sent to my email).
• (5) diversity in the imagery
• (6) I plan for it to be mostly static. I will not be adding/changing regularly (although imagine the first couple months will want to tweak it as I get feedback). I do not plan to add blogs, etc.
Nice to have
• (1) Good graphics. I'm ok with black and white if it's classic or color photos. I don't want stalk photos anyone can get on the web. A sophisticated yet approachable look is what I'm going for.
• (2) Ability to get to know me (the principal) just a bit. That can be through the verbiage, colors, photos, etc.
• (3) Ability to contact me from the front home/landing page or contact page.
• (4) When someone looks me up on line, I want them to see a sentence or two about the company and have links that will take them straight to the page on the website they are looking for (contact, about us, etc.)
Should not have
• I do not want this to be:
• (1) overly feminine (not pink, purple, etc.),
• (2) flashy (I'm fine with a small video or moving photo but doubt I want anything beyond that) or
• (3) too close to the "out there" category (this is a professional business with corporate clients).
• (4) sterile (I'm selling myself .. that's what people buy when they hire a consultant).
• (5) basic - I do not want this to look like I hired my nephew straight out of college to build this. I'm looking for a strong, professional look.

```html
<!DOCTYPE html>
<html lang="en">
<head>
<meta charset="utf-8">
<title>Whitmore Talent Solutions</title>
<link rel="stylesheet" href="https://fonts.googleapis.com/css2?family=Poppins:wght@400;500;600;700&family=Open+Sans:wght@400;600&display=swap">
<style>
:root{
  --backdrop:#6ee4c4;
  --blue:#1a7cf5;
  --blue-dark:#0f66db;
  --blue-soft:#eaf2fe;
  --ink:#1d2333;
  --muted:#8a93a6;
  --white:#ffffff;
  --line:#e3e9f3;
  --map:#e9eaec;
}
*{margin:0;padding:0;box-sizing:border-box}
html,body{width:1200px;height:3000px;overflow:hidden;background:var(--backdrop)}
body{font-family:"Open Sans",sans-serif;color:var(--ink);position:relative}
.page{position:absolute;left:346px;top:99px;width:508px;height:2803px;background:var(--white);overflow:hidden}
.abs{position:absolute}
h1,h2,h3,h4,.num{font-family:"Poppins",sans-serif}
.fill{position:absolute}
.photo-blue{background:linear-gradient(160deg,#8fb8e8,#2b5fa8)}
.photo-office{background:linear-gradient(150deg,#cfd8e2,#8d9aa8)}
.photo-warm{background:linear-gradient(150deg,#e6dccf,#a79a8a)}
.small{font-size:3.4px;line-height:5.2px;color:var(--muted)}
.btn{position:absolute;background:var(--blue);color:var(--white);font-family:"Poppins",sans-serif;font-weight:600;border-radius:10px;text-align:center}
.link{color:var(--blue);font-size:3.6px;font-weight:600}

/* header */
.hero-band{left:0;top:0;width:508px;height:256px;background:var(--blue)}
.brand{left:97px;top:5px;display:flex;align-items:center;gap:3px;color:var(--white);font-family:"Poppins",sans-serif;font-size:4.6px;line-height:5px;font-weight:500}
.brand-mark{width:15px;height:15px;border:1.4px solid var(--white);border-radius:50%}
.nav{left:249px;top:13px;display:flex;gap:0;color:var(--white);font-family:"Poppins",sans-serif;font-size:5.6px}
.nav span{position:absolute;white-space:nowrap}
.social{left:439px;top:15px;display:flex;gap:6px}
.social i{width:4px;height:4px;border-radius:50%;background:rgba(255,255,255,.7);display:block}
.hero-card{left:26px;top:31px;width:455px;height:229px;background:var(--white)}
.hero-photo{left:33px;top:41px;width:189px;height:219px}
.eyebrow{left:233px;top:117px;font-size:5.4px;color:var(--blue);letter-spacing:.2px}
.hero-title{left:233px;top:126px;font-size:20px;line-height:23px;font-weight:700}
.hero-text{left:233px;top:180px;width:90px}
.hero-btn{left:233px;top:211px;width:42px;height:11px;border:.8px solid var(--line);border-radius:6px;font-size:3.4px;color:var(--blue);text-align:center;line-height:10px;background:var(--white)}
.play{left:283px;top:211px;width:12px;height:12px;border-radius:50%;background:var(--blue)}

/* why */
.why-title{left:106px;top:288px;font-size:9px;font-weight:700}
.why-text{left:106px;top:306px;width:88px}
.card{position:absolute;background:var(--white);box-shadow:0 1px 6px rgba(40,80,160,.12);text-align:center;padding-top:12px}
.card .ic{width:12px;height:12px;border-radius:50%;background:var(--blue);margin:0 auto 6px}
.card h4{font-size:7px;font-weight:600;margin-bottom:4px}
.card .small{padding:0 8px}

/* bio */
.bio-band{left:0;top:504px;width:508px;height:182px;background:var(--blue)}
.soft-band{left:0;top:686px;width:508px;height:383px;background:var(--blue-soft)}
.bio-photo{left:105px;top:531px;width:147px;height:182px}
.bio-text{left:259px;top:534px;width:208px;font-size:5.6px;line-height:6.4px;color:var(--white)}
.bio-name{left:259px;top:645px;font-family:"Poppins",sans-serif;font-size:5.6px;font-weight:700;color:var(--white)}
.bio-role{left:259px;top:652px;font-size:5.6px;color:var(--white)}
.quote-link{left:266px;top:696px;display:flex;align-items:center;gap:3px;font-family:"Poppins",sans-serif;font-weight:600;font-size:5.4px}
.quote-link i{width:15px;height:15px;border:1px solid var(--blue);border-radius:50%}

.sec-title{left:0;width:508px;text-align:center;font-size:11px;font-weight:600}
.sec-sub{left:174px;width:160px;text-align:center}
.svc{position:absolute;left:107px;width:294px;height:64px;background:var(--white)}
.svc .fill{left:0;top:0;width:112px;height:64px}
.svc h4{position:absolute;left:123px;top:8px;font-size:5.6px;font-weight:600}
.svc .small{position:absolute;left:123px;top:20px;width:150px}
.svc .link{position:absolute;left:123px;top:48px}
.cta{left:107px;top:1028px;width:294px;height:40px;background:var(--blue);color:var(--white);font-size:5.6px;font-weight:600;padding:17px 11px}
.cta-btn{left:365px;top:1043px;width:40px;height:12px;background:var(--white);color:var(--blue);font-size:4.6px;line-height:12px;border-radius:6px}

/* cases */
.filters{left:0;top:1154px;width:508px;text-align:center;font-size:3.4px;color:var(--muted);word-spacing:2px}
.case{position:absolute;width:93px;height:120px}
.case-label{left:8px;top:82px;color:var(--white);font-family:"Poppins",sans-serif;font-size:5.4px;font-weight:600;line-height:6px}

.dots{position:absolute;width:44px;height:30px;background-image:radial-gradient(circle,#b9d1f6 1.2px,transparent 1.4px);background-size:11px 11px}
.p-title{left:274px;top:1455px;font-size:10.5px;line-height:12px;font-weight:600}
.p-text{left:274px;top:1484px;width:128px}

/* stats */
.stats{left:0;top:1648px;width:508px;height:89px;background:var(--blue);color:var(--white)}
.stat{position:absolute;top:28px;width:80px;margin-left:-40px;text-align:center}
.stat .num{font-size:19px;font-weight:600;line-height:20px}
.stat .num small{font-size:12px}
.stat p{font-size:7.6px}

/* testimonial */
.t-frame{left:107px;top:1749px;width:118px;height:156px;background:var(--blue)}
.t-photo{left:122px;top:1768px;width:103px;height:137px}
.t-title{left:241px;top:1750px;font-size:10px;line-height:12px;font-weight:600}
.t-text{left:241px;top:1785px;width:155px;font-style:italic}
.t-name{left:241px;top:1880px;font-family:"Poppins",sans-serif;font-size:6px;font-weight:600}
.t-role{left:241px;top:1889px;font-size:6px;color:var(--muted)}
.stars{left:241px;top:1902px;display:flex;gap:4px}
.stars i{width:3px;height:3px;border-radius:50%;background:var(--blue)}

/* partners */
.partners{left:0;top:1937px;width:508px;height:101px;background:var(--blue)}
.partner{position:absolute;top:33px;height:37px;border:1px solid rgba(255,255,255,.5);background:rgba(255,255,255,.18);color:#bcd8ff;font-family:"Poppins",sans-serif;font-weight:600;font-size:8px;text-align:center;line-height:35px}

/* contact */
.c-wash{left:0;top:2110px;width:508px;height:293px;background:linear-gradient(180deg,#eaf2fe,#ffffff)}
.c-illus{left:27px;top:2074px;width:200px;height:139px;border-radius:6px;background:linear-gradient(135deg,#dbe8fd,#8fb7f7)}
.c-title{left:273px;top:2066px;font-size:10px;font-weight:600}
.c-text{left:273px;top:2084px;width:125px}
.field{position:absolute;left:273px;width:144px;height:18px;background:var(--white);border:.7px solid var(--line);border-radius:3px;font-size:4px;color:var(--muted);padding:5px 9px}
.send{left:273px;top:2222px;width:52px;height:13px;font-size:4px;line-height:13px}
.info{position:absolute;top:2268px;width:93px;height:70px;background:var(--white);box-shadow:0 1px 6px rgba(40,80,160,.12);padding:12px 8px}
.info h4{font-size:7px;font-weight:600;display:flex;align-items:center;gap:4px;margin-bottom:6px}
.info h4 svg{width:13px;height:13px}
.emerg{left:0;top:2352px;width:508px;text-align:center;font-size:7.6px;color:#4d5568}
.emerg-num{left:0;top:2364px;width:508px;text-align:center;font-size:7.6px;color:var(--blue);font-weight:600}
.map{left:0;top:2403px;width:508px;height:183px;background:var(--map)}

/* footer */
.f-brand{left:211px;top:2613px;display:flex;align-items:center;gap:4px;color:var(--blue);font-family:"Poppins",sans-serif;font-size:5.4px;line-height:6px}
.f-brand i{width:20px;height:20px;border:1.4px solid var(--blue);border-radius:50%;display:block}
.f-rule{left:107px;top:2648px;width:294px;height:1px;background:var(--line)}
.f-col h4{font-size:5.6px;font-weight:600;margin-bottom:5px}
.f-col p{font-size:3.8px;line-height:7.6px;color:var(--muted)}
.f-contact{left:107px;top:2680px;font-size:3.6px;line-height:5px;color:var(--muted)}
.f-contact div{display:flex;gap:4px;margin-bottom:11px}
.f-contact i{width:8px;height:8px;border:1px solid var(--blue);border-radius:50%;flex:none}
.world{left:319px;top:2684px;width:82px;height:36px;border-radius:4px;background:linear-gradient(90deg,#d3e3fb,#a8c7f6)}
.f-bar{left:0;top:2767px;width:508px;height:36px;background:var(--blue)}
.up{left:247px;top:2760px;width:14px;height:14px;border-radius:50%;background:var(--white);box-shadow:0 1px 4px rgba(0,0,0,.15)}
</style>
</head>
<body>
<main class="page">

<header>
  <div class="abs hero-band"></div>
  <div class="abs brand"><span class="brand-mark"></span><span>WHITMORE<br>TALENT<br>SOLUTIONS</span></div>
  <nav class="abs nav">
    <span style="left:0">Home</span><span style="left:39px">My Bio</span><span style="left:77px">Services</span><span style="left:116px">About</span><span style="left:153px">Contact</span>
  </nav>
  <div class="abs social"><i></i><i></i><i></i><i></i></div>
  <div class="abs hero-card"></div>
  <div class="fill hero-photo photo-blue" role="img" aria-label="Portrait of the principal consultant"></div>
  <p class="abs eyebrow">I WANT TO SEE YOUR SUCCESS</p>
  <h1 class="abs hero-title">Your Success<br>&nbsp;My Business</h1>
  <p class="abs hero-text small">Trusted guidance for senior leaders and boards through every stage of growth.</p>
  <div class="abs hero-btn">How Can I Help You</div>
  <div class="abs play"><svg width="12" height="12" viewBox="0 0 12 12"><path d="M5 4l3 2-3 2z" fill="#fff"/></svg></div>
</header>

<section>
  <h2 class="abs why-title">Why Choose Me?</h2>
  <p class="abs why-text small">Three decades of executive development work, bringing clear insight and steady counsel to every leadership team.</p>
  <div class="btn" style="left:106px;top:343px;width:59px;height:15px;font-size:5px;line-height:15px">Read More</div>
  <div class="card" style="left:206px;top:288px;width:94px;height:88px"><div class="ic"></div><h4>My Services</h4><p class="small">Coaching, assessment and transition support built around your goals and people.</p><p class="link" style="margin-top:4px">Read More</p></div>
  <div class="card" style="left:206px;top:384px;width:94px;height:88px"><div class="ic"></div><h4>My Approach</h4><p class="small">Practical, candid work that connects talent plans with business strategy.</p><p class="link" style="margin-top:4px">Read More</p></div>
  <div class="card" style="left:306px;top:341px;width:95px;height:90px"><div class="ic"></div><h4>Advantage Results</h4><p class="small">Stronger leaders, smoother successions and teams ready for what comes next.</p><p class="link" style="margin-top:4px">Read More</p></div>
</section>

<section>
  <div class="abs bio-band"></div>
  <div class="abs soft-band"></div>
  <div class="fill bio-photo photo-warm" role="img" aria-label="Photo of the principal consultant"></div>
  <p class="abs bio-text">Claire Whitmore is a highly respected and sought-after talent management expert focused on the full talent ecosystem. Her depth of expertise includes talent management, assessment, succession planning, organizational development, as well as identifying and developing critical talent. She quickly and effectively connects talent strategies to business strategies, coaching and advising leaders to increase their effectiveness while staying aligned to company goals. Claire has worked extensively with global professionals with an emphasis on executives including CEOs and Boards of Directors. She is routinely asked to coach and counsel senior leaders to improve their performance and therefore the organizations' success.</p>
  <p class="abs bio-name">Claire Whitmore</p>
  <p class="abs bio-role">Chairman</p>
  <div class="abs quote-link"><i></i>See Chairman Quote</div>

  <h2 class="abs sec-title" style="top:733px">Services</h2>
  <p class="abs sec-sub small" style="top:762px">Focused support for leaders, teams and boards at every stage of change.</p>
  <div class="svc" style="top:790px"><div class="fill photo-office" role="img" aria-label="Colleagues working in an office"></div><h4>Human Resource Help</h4><p class="small">Practical guidance on talent processes, team structure and people strategy for growing firms.</p><span class="link">Read More</span></div>
  <div class="svc" style="top:861px"><div class="fill photo-office" role="img" aria-label="Team meeting at a desk"></div><h4>Finance Help</h4><p class="small">Aligning leadership plans and budgets so people investments support business results.</p><span class="link">Read More</span></div>
  <div class="svc" style="top:933px"><div class="fill photo-office" role="img" aria-label="Leader working at a laptop"></div><h4>counsel senior leaders</h4><p class="small">One-to-one coaching and assessment for executives, CEOs and new board members.</p><span class="link">Read More</span></div>
  <div class="abs cta">Are you looking for professional advice for your business?</div>
  <div class="btn cta-btn abs">Get In Touch</div>
</section>

<section>
  <h2 class="abs sec-title" style="top:1096px">Latest Case Studies</h2>
  <p class="abs sec-sub small" style="top:1121px">Selected work with leaders and boards across many industries.</p>
  <p class="abs filters"><span style="color:var(--blue)">All</span> Business Analysis Consumer Products Consumer Financial Analysis Travel &amp; Aviation</p>
  <div class="case" style="left:107px;top:1173px;background:linear-gradient(180deg,#cfe0fb,#1a7cf5)" role="img" aria-label="Business team case study"><p class="abs case-label">Becoming a living<br>business</p><span class="abs" style="left:8px;top:102px;width:10px;height:10px;border-radius:50%;background:#fff"></span></div>
  <div class="case photo-office" style="left:207px;top:1173px" role="img" aria-label="Handshake between colleagues"></div>
  <div class="case photo-office" style="left:308px;top:1173px" role="img" aria-label="Colleagues reviewing a laptop"></div>
  <div class="case photo-office" style="left:107px;top:1301px" role="img" aria-label="Team discussion at a table"></div>
  <div class="case photo-office" style="left:207px;top:1301px" role="img" aria-label="Meeting in a conference room"></div>
  <div class="case photo-warm" style="left:308px;top:1301px" role="img" aria-label="Professional working on the floor with papers"></div>
</section>

<section>
  <div class="dots" style="left:107px;top:1457px"></div>
  <div class="dots" style="left:206px;top:1575px"></div>
  <div class="fill photo-warm" style="left:149px;top:1454px;width:110px;height:101px" role="img" aria-label="Professional working at a desk"></div>
  <div class="fill photo-blue" style="left:107px;top:1501px;width:98px;height:115px" role="img" aria-label="Consultant seated with a laptop"></div>
  <h2 class="abs p-title">A passion for<br>Consulting Services</h2>
  <p class="abs p-text small">Every engagement starts with listening. I take time to understand your people, your culture and the pressures facing your leaders before shaping a plan that fits.<br><br>The result is candid, practical advice that helps leaders grow and keeps the organization moving forward.</p>
  <div class="btn" style="left:274px;top:1571px;width:41px;height:15px;font-size:4px;line-height:15px">Read More</div>
</section>

<section class="abs stats">
  <div class="stat" style="left:134px"><div class="num">569</div><p>Happy Client</p></div>
  <div class="stat" style="left:213px"><div class="num">100%</div><p>Satisfaction</p></div>
  <div class="stat" style="left:291px"><div class="num">85<small>k</small></div><p>Total Project</p></div>
  <div class="stat" style="left:371px"><div class="num">4.5</div><p>Client Review</p></div>
</section>

<section>
  <div class="abs t-frame"></div>
  <div class="fill t-photo photo-office" role="img" aria-label="Client holding a folder"></div>
  <h2 class="abs t-title">What's Our Client Says<br>About Us</h2>
  <p class="abs t-text small">Claire brought clarity to a difficult leadership transition. Her coaching helped our new team settle quickly, and her honest feedback made every conversation more useful. We would not hesitate to work with her again on our next succession plan and board review.</p>
  <p class="abs t-name">Daniel Ames</p>
  <p class="abs t-role">CEO ABC Company</p>
  <div class="abs stars"><i></i><i></i><i></i><i></i><i></i></div>
</section>

<section class="abs partners">
  <div class="partner" style="left:107px;width:67px">Summit</div>
  <div class="partner" style="left:183px;width:66px">Brightway</div>
  <div class="partner" style="left:259px;width:66px">Northfield</div>
  <div class="partner" style="left:333px;width:68px">Lakeside</div>
</section>

<section>
  <div class="abs c-wash"></div>
  <div class="fill c-illus" role="img" aria-label="Illustration of a support agent at a laptop with chat bubbles"></div>
  <h2 class="abs c-title">Hello With Us</h2>
  <p class="abs c-text small">Share a few details about your needs and I will reply within two business days.</p>
  <div class="field" style="top:2128px">Your Name *</div>
  <div class="field" style="top:2154px">Your Email *</div>
  <div class="field" style="top:2181px">Message</div>
  <div class="btn send">Send Message</div>

  <div class="info" style="left:107px"><h4><svg viewBox="0 0 14 14"><path d="M7 13s-4-4.5-4-7.5a4 4 0 018 0C11 8.5 7 13 7 13z" fill="none" stroke="#1a7cf5"/><circle cx="7" cy="5.5" r="1.5" fill="none" stroke="#1a7cf5"/></svg>Address</h4><p class="small">Suite 410, 88 Harbor Lane, Oakridge County</p></div>
  <div class="info" style="left:207px"><h4><svg viewBox="0 0 14 14"><rect x="1.5" y="3.5" width="11" height="7.5" fill="none" stroke="#1a7cf5"/><path d="M1.5 3.5L7 8l5.5-4.5" fill="none" stroke="#1a7cf5"/></svg>Email</h4><p class="small">hello@whitmoretalent.com<br>office@whitmoretalent.com</p></div>
  <div class="info" style="left:308px"><h4><svg viewBox="0 0 14 14"><path d="M3 2h2.5l1 3-1.5 1a7 7 0 003 3l1-1.5 3 1V11a1 1 0 01-1 1A10 10 0 012 3a1 1 0 011-1z" fill="none" stroke="#1a7cf5"/></svg>Toll Free</h4><p class="small">1800 - 4400 - 5500<br>1800 - 4400 - 5511</p></div>
  <p class="abs emerg">Call us for any emergency to this number</p>
  <p class="abs emerg-num">1800 - 4400 - 5500</p>
</section>

<div class="fill map" role="img" aria-label="Street map showing the office location"></div>

<footer>
  <div class="abs f-brand"><i></i><span>WHITMORE<br>TALENT<br>SOLUTIONS</span></div>
  <div class="abs f-rule"></div>
  <div class="abs f-contact">
    <div><i></i><span>Suite 410, 88 Harbor Lane<br>Oakridge County</span></div>
    <div><i></i><span>1800 - 4400 - 5500<br>1800 - 4400 - 5511</span></div>
    <div><i></i><span>hello@whitmoretalent.com<br>office@whitmoretalent.com</span></div>
  </div>
  <div class="abs f-col" style="left:196px;top:2667px"><h4>Our Services</h4><p>Leader Coaching<br><span style="color:var(--blue)">General Consultancy</span><br>Board Advisory<br>Online Consulting<br>Business Consulting<br>CEO Transition</p></div>
  <div class="abs f-col" style="left:264px;top:2667px"><h4>Quick Link</h4><p>About Us<br>Services<br>FAQ<br>Privacy policy<br>Support<br>Contact</p></div>
  <div class="abs f-col" style="left:319px;top:2667px"><h4>Our Footprint</h4></div>
  <div class="fill world" role="img" aria-label="World map with office locations"></div>
  <div class="abs f-bar"></div>
  <div class="abs up"><svg width="14" height="14" viewBox="0 0 14 14"><path d="M4.5 8L7 5.5 9.5 8" fill="none" stroke="#1a7cf5" stroke-width=".8"/></svg></div>
</footer>

</main>
</body>
</html>
```